General Contractors need a new Crisp updated Card Design

We need a new business card design for our company of 25 years based in Toronto call Holvaster Building Inc. : Our goal is to be the leading commercial contractors in Toronto by providing exceptional value to our clients. We work very hard to deliver professional, quality, service in conjunction with consistent price competitiveness to all of our clients on every single project.

Target Market(s)

Design & Build Clients

Industry/Entity Type

Construction Company

Contact Information for Business Card

Address:
18 North Tamlin Glen Road, Unit 57, Marbrook Vale, ON, K7T 2R9
Office: 905-218-5937

Holvasters Logo
Employee Job Description
Employee Cell Phone #
Employee Email
www.holvaster-example.com

Colors

Designer to choose colors to be used in the design.

Requirements
Must have
• Quote Company Saying:
• "Professional. Quality. Service."
Nice to have
• New Crisp up to date look. simple & fresh ( Not to Busy)
Should not have
• NO BLUE PRINTS ON THE BUSINESS CARDS

```html
<!DOCTYPE html>
<html lang="en">
<head>
<meta charset="utf-8">
<title>Holvaster Building Inc. – Business Card</title>
<link rel="stylesheet" href="https://fonts.googleapis.com/css2?family=Caladea:wght@400;700&display=swap">
<style>
  :root {
    --page-bg: #e9e7e3;
    --card-bg: #f7f8f6;
    --brand-green: #17695c;
    --swoosh-silver: #a9bdb5;
    --swoosh-light: #d3ddd8;
    --contact-text: #eadfc4;
    --title-text: #3a3a3a;
  }
  * { margin: 0; padding: 0; box-sizing: border-box; }
  html, body {
    width: 1200px; height: 1054px; overflow: hidden;
    background: var(--page-bg);
    font-family: "Caladea", Georgia, serif;
  }
  .business-card {
    position: absolute; left: 100px; top: 225px;
    width: 1000px; height: 604px;
    background: var(--card-bg);
    overflow: hidden;
    box-shadow: 0 10px 30px rgba(0,0,0,0.18);
  }
  .card-waves { position: absolute; inset: 0; }
  .brand-block {
    position: absolute; left: 60px; top: 72px; width: 380px;
    display: flex; flex-direction: column; align-items: center;
  }
  .brand-square {
    width: 160px; height: 160px; background: var(--brand-green);
  }
  .brand-name {
    margin-top: 30px;
    color: var(--brand-green);
    font-weight: 700; font-size: 42px; line-height: 1.05;
    letter-spacing: 1px; text-align: center;
  }
  .company-saying {
    margin-top: 14px;
    color: var(--brand-green);
    font-size: 17px; letter-spacing: 3px;
    text-transform: uppercase; text-align: center; white-space: nowrap;
  }
  .person {
    position: absolute; right: 55px; top: 84px; text-align: right;
  }
  .person-name {
    color: var(--brand-green); font-weight: 700; font-size: 38px; line-height: 1;
  }
  .person-title {
    margin-top: 10px; color: var(--title-text); font-size: 22px;
  }
  .contact-list {
    position: absolute; right: 55px; top: 352px; list-style: none;
    color: var(--contact-text); font-size: 24px; text-align: right;
  }
  .contact-list li {
    height: 33px; display: flex; justify-content: flex-end; align-items: center; gap: 12px;
  }
  .contact-icon { width: 20px; height: 20px; flex: none; }
  .address {
    position: absolute; right: 55px; top: 498px;
    color: var(--contact-text); font-size: 24px; line-height: 33px;
    text-align: right; font-style: normal;
  }
</style>
</head>
<body>
  <main class="business-card">
    <svg class="card-waves" viewBox="0 0 1000 604" width="1000" height="604" aria-hidden="true">
      <path d="M0,540 C260,560 430,520 570,430 C690,352 820,298 1000,288 L1000,604 L0,604 Z" fill="var(--brand-green)"/>
      <path d="M0,470 C200,500 380,470 520,380 C650,300 800,262 1000,252" fill="none" stroke="var(--swoosh-light)" stroke-width="26"/>
      <path d="M0,490 C220,520 400,488 540,396 C670,312 820,276 1000,266" fill="none" stroke="var(--swoosh-silver)" stroke-width="10"/>
      <path d="M40,505 C240,525 380,505 470,470" fill="none" stroke="var(--swoosh-silver)" stroke-width="6"/>
      <path d="M0,520 C180,545 360,540 470,500" fill="none" stroke="var(--swoosh-light)" stroke-width="8"/>
    </svg>

    <div class="brand-block">
      <div class="brand-square"></div>
      <div class="brand-name">HOLVASTER<br>BUILDING INC.</div>
      <div class="company-saying">Professional. Quality. Service.</div>
    </div>

    <div class="person">
      <div class="person-name">Marcus Delane</div>
      <div class="person-title">Managing Director</div>
    </div>

    <ul class="contact-list">
      <li>416-730-2864
        <svg class="contact-icon" viewBox="0 0 20 20"><rect x="5" y="1" width="10" height="18" rx="2" fill="none" stroke="currentColor" stroke-width="2"/><circle cx="10" cy="15.5" r="1.2" fill="currentColor"/></svg>
      </li>
      <li>905-218-5937
        <svg class="contact-icon" viewBox="0 0 20 20"><path d="M2,8 C2,4 18,4 18,8 L15,9 L14,7 L6,7 L5,9 Z" fill="currentColor"/><path d="M5,10 L15,10 L17,17 L3,17 Z" fill="currentColor"/></svg>
      </li>
      <li>marcus.d@holvaster-example.com
        <svg class="contact-icon" viewBox="0 0 20 20"><rect x="1" y="4" width="18" height="12" fill="currentColor"/><path d="M1,4 L10,11 L19,4" fill="none" stroke="var(--brand-green)" stroke-width="1.5"/></svg>
      </li>
      <li>www.holvaster-example.com
        <svg class="contact-icon" viewBox="0 0 20 20" fill="none" stroke="currentColor" stroke-width="1.5"><circle cx="10" cy="10" r="8"/><ellipse cx="10" cy="10" rx="3.5" ry="8"/><line x1="2" y1="10" x2="18" y2="10"/></svg>
      </li>
    </ul>

    <address class="address">18 North Tamlin Glen Road, Unit 57<br>Marbrook Vale, ON, K7T 2R9</address>
  </main>
</body>
</html>
```